Virtual background for e-learning webinar presenter

I would like to create a virtual background for our webinar presentations. I would like it to have a background of a modern surgical suite with our logo. The surgical suite that I have included is free for public use.

Our company is called pawcrestlearn.com.

Target Market(s)

Primary care veterinarians

Font styles to use
Sans Serif

Requirements
Must have
• Must look professional. We are promoting a e-learning platform for veterinarians. Must look like an elite modern professional educational platform.
Nice to have
• Modern surgical suite. Match existing logo which has been provided.
Should not have
• Other than our logo, no cutesy dogs, cats or puppies

```html
<!DOCTYPE html>
<html lang="en">
<head>
<meta charset="utf-8">
<title>PawcrestLearn Webinar Background</title>
<link href="https://fonts.googleapis.com/css2?family=Montserrat:wght@600&display=swap" rel="stylesheet">
<style>
  :root {
    --suite-deep: #0b3f8f;
    --suite-mid: #1f86d6;
    --suite-light: #3fc3ec;
    --line-blue: #1f4fe0;
    --line-green: #2ed59a;
    --line-cyan: #55c8f0;
    --ring-green: #33d69b;
    --ring-red: #d8465c;
    --ring-orange: #e9874a;
    --ring-blue: #2c8de6;
    --logo-panel: #dbe4ee;
    --logo-text: #1f7fd0;
    --window-top: #d9dcef;
    --window-mid: #8c92c4;
    --window-low: #5a5f96;
  }
  * { margin: 0; padding: 0; box-sizing: border-box; }
  html, body { width: 1200px; height: 578px; overflow: hidden; background: #0e4fa0; }
  .webinar-backdrop {
    position: relative;
    width: 1200px;
    height: 578px;
    overflow: hidden;
    font-family: "Montserrat", sans-serif;
  }
  .suite-backdrop {
    position: absolute;
    inset: 0;
    background:
      radial-gradient(ellipse at 50% 85%, var(--suite-light) 0%, transparent 55%),
      radial-gradient(ellipse at 85% 20%, #2a9be0 0%, transparent 45%),
      linear-gradient(180deg, var(--suite-deep) 0%, var(--suite-mid) 55%, var(--suite-light) 100%);
  }
  .stage-lines {
    position: absolute;
    inset: 0;
    width: 1200px;
    height: 578px;
  }
  .logo-panel {
    position: absolute;
    left: 236px;
    top: 0;
    width: 168px;
    height: 147px;
    background: var(--logo-panel);
    display: flex;
    align-items: center;
    justify-content: center;
    gap: 6px;
  }
  .logo-mark {
    width: 10px;
    height: 10px;
    background: var(--logo-text);
  }
  .logo-name {
    color: var(--logo-text);
    font-weight: 600;
    font-size: 15px;
    letter-spacing: -0.2px;
  }
  .suite-window {
    position: absolute;
    left: 320px;
    top: 82px;
    width: 586px;
    height: 408px;
    border-radius: 50%;
    background: conic-gradient(from 0deg, var(--ring-green), var(--ring-red) 30%, var(--ring-orange) 55%, var(--ring-blue) 72%, var(--ring-green));
    filter: blur(0.6px);
    box-shadow: 0 0 18px rgba(60, 160, 240, 0.6);
  }
  .suite-window-inner {
    position: absolute;
    left: 14px;
    top: 14px;
    right: 14px;
    bottom: 14px;
    border-radius: 50%;
    background: var(--ring-blue);
    padding: 10px;
  }
  .suite-photo {
    width: 100%;
    height: 100%;
    border-radius: 50%;
    background:
      radial-gradient(ellipse at 50% 30%, var(--window-top) 0%, transparent 40%),
      radial-gradient(ellipse at 50% 80%, #eef0fa 0%, transparent 35%),
      linear-gradient(180deg, var(--window-mid) 0%, var(--window-low) 55%, #c9cde6 100%);
  }
</style>
</head>
<body>
  <main class="webinar-backdrop">
    <div class="suite-backdrop" role="img" aria-label="Softly blurred modern surgical suite in blue light"></div>

    <svg class="stage-lines" viewBox="0 0 1350 650" preserveAspectRatio="none" aria-hidden="true">
      <g fill="none" stroke-linecap="butt">
        <polyline points="0,150 300,300 0,470" stroke="var(--line-cyan)" stroke-width="10" opacity="0.5"/>
        <polyline points="0,210 240,320 0,420" stroke="var(--line-cyan)" stroke-width="8" opacity="0.4"/>
        <polyline points="1350,150 1050,300 1350,470" stroke="var(--line-cyan)" stroke-width="10" opacity="0.5"/>
        <polyline points="1350,210 1110,320 1350,420" stroke="var(--line-cyan)" stroke-width="8" opacity="0.4"/>
        <line x1="0" y1="30" x2="1350" y2="640" stroke="var(--line-blue)" stroke-width="10"/>
        <line x1="0" y1="80" x2="1350" y2="590" stroke="var(--line-green)" stroke-width="10"/>
        <line x1="1350" y1="30" x2="0" y2="640" stroke="var(--line-blue)" stroke-width="10"/>
        <line x1="1350" y1="80" x2="0" y2="590" stroke="var(--line-green)" stroke-width="10"/>
      </g>
    </svg>

    <div class="suite-window">
      <div class="suite-window-inner">
        <div class="suite-photo" role="img" aria-label="Modern surgical suite with ring light, operating table and wall monitors"></div>
      </div>
    </div>

    <div class="logo-panel">
      <span class="logo-mark"></span>
      <span class="logo-name">pawcrestlearn.com</span>
    </div>
  </main>
</body>
</html>
```